Nurturing Victors 6x9 book soft cover- front cover only

We need a book cover for a softcover book. We will need final files in Photoshop or InDesign is preferred.

Overall Title:
Nurturing Victors
Subtitle:
The Foundations of Humble Mentoring for Trainers, Instructors and Players
Author:
by Dr. Martin Hollis

The audience is high school and college coaches however we don't want the standard picture with words over the top. Make it a creative design but keep it mind it's a little academic.

```html
<!DOCTYPE html>
<html lang="en">
<head>
<meta charset="UTF-8">
<title>Nurturing Victors – Front Cover</title>
<link rel="stylesheet" href="https://fonts.googleapis.com/css2?family=Alfa+Slab+One&family=Barlow:wght@500&display=swap">
<style>
  :root {
    --page-bg: #f2f2f2;
    --cover-red: #d0161a;
    --cover-red-deep: #b80f13;
    --panel-dark: #262626;
    --panel-darker: #141414;
    --gold-light: #fff1a8;
    --gold-mid: #e5c05a;
    --gold-deep: #8a6414;
    --title-shadow: rgba(90, 10, 10, 0.55);
    --text-light: #ffffff;
  }
  * { margin: 0; padding: 0; box-sizing: border-box; }
  html, body {
    width: 1200px;
    height: 850px;
    overflow: hidden;
    background: var(--page-bg);
  }
  .canvas {
    position: relative;
    width: 1200px;
    height: 850px;
    display: flex;
    align-items: center;
    justify-content: center;
  }
  .cover {
    position: relative;
    width: 520px;
    height: 780px;
    background: linear-gradient(160deg, var(--cover-red) 0%, var(--cover-red) 60%, var(--cover-red-deep) 100%);
    overflow: hidden;
  }
  .emblem-area {
    position: absolute;
    left: 80px;
    top: 160px;
    width: 360px;
    height: 430px;
    border-radius: 6px;
    background: linear-gradient(180deg, var(--panel-dark) 0%, var(--panel-darker) 100%);
  }
  .subtitle {
    position: absolute;
    left: 0;
    width: 100%;
    top: 272px;
    text-align: center;
    font-family: "Barlow", sans-serif;
    font-weight: 500;
    font-size: 17px;
    line-height: 1.35;
    color: var(--text-light);
    letter-spacing: 0.3px;
  }
  .title {
    position: absolute;
    left: 0;
    width: 100%;
    top: 326px;
    text-align: center;
    font-family: "Alfa Slab One", serif;
    font-weight: 400;
    font-size: 54px;
    line-height: 1.12;
    text-transform: uppercase;
    letter-spacing: 1px;
    background: linear-gradient(180deg, var(--gold-light) 0%, var(--gold-mid) 45%, var(--gold-deep) 100%);
    -webkit-background-clip: text;
    background-clip: text;
    color: transparent;
    filter: drop-shadow(0 3px 2px var(--title-shadow));
  }
  .author {
    position: absolute;
    left: 0;
    width: 100%;
    bottom: 62px;
    text-align: center;
    font-family: "Barlow", sans-serif;
    font-weight: 500;
    font-size: 21px;
    color: var(--text-light);
    letter-spacing: 0.4px;
  }
</style>
</head>
<body>
  <main class="canvas">
    <section class="cover">
      <div class="emblem-area" role="img" aria-label="Central emblem artwork: a dark shield with a gold frame"></div>
      <p class="subtitle">The Foundations of Humble Mentoring<br>for Trainers, Instructors and Players</p>
      <h1 class="title">Nurturing<br>Victors</h1>
      <p class="author">Dr. Martin Hollis</p>
    </section>
  </main>
</body>
</html>
```